Invitation Design Project

In May 2014, my husband and I celebrate our 10th wedding anniversary, and in June 2014 I celebrate my 40th birthday. We will be having a "10/40" party in June 2014 for both events.

This party will be held on my property, "Tallowmere Farm" in North Queensland, so the invitation needs to be fun, whimsical and reflective of both our farm and the Australian bush. You can see photos of our property on facebook: https://www.plinkspace.example/tallowmerefarm

The party will be held on 7 June 2014, RSVP by 1 April 2014.

Target Market(s)

Our family and friends - all ages and backgrounds

Industry/Entity Type

Wedding

Requirements
Must have
• Must have the following details: (wording is flexible)
- Wendy & Martin celebrate their 10th wedding anniversary on 8 May 2014.
- Wendy turns 40 on 9 June 2014
- Party to be held on Tallowmere Farm, 6pm start. Dinner, entertainment and courtesy bus provided, BYO drinks.
- RSVP by 1 April 2014
Must have correct spelling and grammar on the first draft please.
Nice to have
• It might be fun if the invitation could include our pets (dogs, cats, goats, pigs, chickens, parrakeet - see pictures on the facebook link above) in some way, in cartoon form in the background maybe?
Should not have
• I'm not particularly interested in having our photos incorporated into the invitation.

```html
<!DOCTYPE html>
<html lang="en">
<head>
<meta charset="utf-8">
<title>Wendy &amp; Martin — 10/40 Invitation</title>
<link rel="stylesheet" href="https://fonts.googleapis.com/css2?family=Amatic+SC:wght@400;700&family=Shadows+Into+Light&family=Sacramento&display=swap">
<style>
  :root {
    --page: #ffffff;
    --paper: #efe1c8;
    --rust: #a9561f;
    --ink: #2a1812;
    --cream: #f4e4c9;
  }
  * { margin: 0; padding: 0; box-sizing: border-box; }
  html, body { width: 1200px; height: 1000px; overflow: hidden; background: var(--page); }
  .invitation {
    position: absolute; left: 415px; top: 68px; width: 412px; height: 869px;
    background: var(--paper); color: var(--ink);
    font-family: "Shadows Into Light", cursive;
  }
  .invitation > * { position: absolute; white-space: nowrap; }
  .rule { background: var(--ink); height: 2px; }
  .rule.double { height: 9px; background: none; border-top: 2px solid var(--ink); border-bottom: 2px solid var(--ink); }
  .greeting { left: 43px; top: 56px; font-size: 16px; line-height: 1; }

  .hosts-panel {
    left: 43px; top: 97px; width: 322px; height: 116px;
    background: var(--rust); color: var(--cream);
  }
  .hosts-panel > * { position: absolute; left: 0; width: 100%; text-align: center; white-space: nowrap; }
  .hosts-names { top: 8px; font-family: "Amatic SC", sans-serif; font-weight: 400; font-size: 66px; line-height: 66px; }
  .hosts-line { top: 78px; font-size: 23px; line-height: 28px; letter-spacing: 2px; }

  .years { left: 43px; top: 228px; font-size: 70px; line-height: 70px; color: var(--rust); }
  .wedding { left: 186px; top: 214px; width: 182px; text-align: right; font-family: "Sacramento", cursive; font-size: 64px; line-height: 64px; }
  .anniversary { left: 196px; top: 264px; font-family: "Amatic SC", sans-serif; font-weight: 400; font-size: 34px; line-height: 34px; }
  .birthday { left: 43px; top: 302px; font-family: "Amatic SC", sans-serif; font-weight: 400; font-size: 58px; line-height: 60px; }
  .birthday .accent { color: var(--rust); }
  .birthday sup { font-size: 26px; vertical-align: 24px; text-decoration: underline double; }

  .divider-v { left: 209px; top: 385px; width: 2px; height: 235px; background: var(--ink); }
  .date { left: 43px; top: 384px; width: 166px; text-align: center; }
  .date .big { display: block; font-family: "Amatic SC", sans-serif; font-weight: 400; font-size: 44px; line-height: 44px; }
  .date .small { display: block; font-size: 20px; line-height: 24px; margin: 6px 0 6px; }
  .venue { left: 218px; top: 384px; width: 150px; }
  .venue .time { font-family: "Amatic SC", sans-serif; font-weight: 400; font-size: 44px; line-height: 44px; }
  .venue .time em { font-family: "Sacramento", cursive; font-style: normal; font-size: 40px; }
  .venue .place { color: var(--rust); font-size: 28px; line-height: 30px; margin-top: 4px; text-align: center; }
  .rsvp { left: 212px; top: 508px; width: 156px; text-align: center; }
  .rsvp .big { display: block; font-family: "Amatic SC", sans-serif; font-weight: 400; font-size: 40px; line-height: 40px; }
  .rsvp .by { display: block; color: var(--rust); font-size: 22px; line-height: 26px; margin: 2px 0 4px; }

  .farm-animals { left: 40px; top: 640px; width: 330px; height: 112px; }
  .footer-band {
    left: 40px; top: 752px; width: 330px; height: 70px;
    background: var(--rust); color: var(--cream); text-align: center;
    font-size: 19px; line-height: 24px; padding-top: 10px; letter-spacing: 1px;
  }
</style>
</head>
<body>
<main class="invitation">
  <p class="greeting">dear</p>
  <div class="rule" style="left:43px;top:84px;width:322px"></div>

  <header class="hosts-panel">
    <h1 class="hosts-names">WENDY-&amp;-MARTIN</h1>
    <p class="hosts-line">invite you to celebrate their</p>
  </header>

  <div class="rule double" style="left:43px;top:219px;width:322px"></div>

  <p class="years">10th</p>
  <p class="wedding">wedding</p>
  <p class="anniversary">ANNIVERSARY</p>
  <p class="birthday"><span class="accent">-&amp;-</span> WENDY'S <span class="accent">40<sup>TH</sup></span></p>

  <div class="rule" style="left:43px;top:376px;width:322px"></div>
  <div class="divider-v"></div>

  <section class="date">
    <span class="big">SATURDAY</span>
    <span class="small">- the -</span>
    <span class="big">SEVENTH</span>
    <span class="small">- of -</span>
    <span class="big">JUNE</span>
    <span class="small">- 2014 -</span>
  </section>

  <section class="venue">
    <p class="time">6:00PM <em>at</em></p>
    <p class="place">Tallowmere<br>farm</p>
  </section>

  <div class="rule" style="left:210px;top:500px;width:155px"></div>

  <section class="rsvp">
    <span class="big">PLEASE RSVP</span>
    <span class="by">-BY-</span>
    <span class="big">April 1st '14</span>
  </section>

  <div class="rule double" style="left:43px;top:622px;width:322px"></div>

  <svg class="farm-animals" role="img" aria-label="Illustration of farm animals: a pig, a goose and a gosling" viewBox="0 0 330 112">
    <rect x="0" y="0" width="330" height="112" fill="var(--rust)" opacity="0.55"/>
  </svg>

  <footer class="footer-band">
    dinner and entertainment provided<br>(byo drinks)
  </footer>
</main>
</body>
</html>
```